Business Card Design

Looking for business card designs for a new business. there will be two cards of the same design (both lots of information below in contact info). We would like the logo diagonally across the card with the information split above and below the logo similar to sketch. happy to look at similar alternatives
Please use same colours as in logo design

Industry/Entity Type

Business

Contact Information for Business Card

Colin Marwood
mob - 0498 172 943
ph - 02 6812 4300
fax - 02 6812 4900
email - col@ridgelinetrusses.com.au
14 Larchmont Road, Westdale NSW 2340

Gavin Holloway
mob - 0421 830 576
ph - 02 6812 4300
fax - 02 6812 4900
email - gavin@ridgelinetrusses.com.au

```html
<!DOCTYPE html>
<html lang="en">
<head>
<meta charset="utf-8">
<title>Ridgeline Trusses – Business Card</title>
<link rel="stylesheet" href="https://fonts.googleapis.com/css2?family=Arimo:wght@400;700&family=Cinzel:wght@400&family=Roboto+Condensed:wght@700&display=swap">
<style>
  :root {
    --stage: #1b1c1d;
    --card: #242526;
    --card-edge: #2e2f30;
    --band: #ffffff;
    --band-shade: #e9e9e9;
    --ink-light: #ffffff;
    --ink-dark: #2a2b2c;
    --blue: #1f5fd6;
    --blue-deep: #0c2a9c;
    --blue-light: #5aa9f0;
  }
  * { margin: 0; padding: 0; box-sizing: border-box; }
  html, body {
    width: 1200px; height: 900px; overflow: hidden;
    background: var(--stage);
  }
  .card {
    position: absolute; left: 150px; top: 190px;
    width: 900px; height: 520px;
    background: linear-gradient(160deg, var(--card-edge), var(--card) 55%);
    border-radius: 6px; overflow: hidden;
    color: var(--ink-light);
    font-family: "Arimo", Arial, sans-serif;
  }
  .card__band { position: absolute; inset: 0; }
  .card__name {
    position: absolute; left: 44px; top: 40px;
    font-family: "Cinzel", serif; font-weight: 400;
    font-size: 36px; letter-spacing: 1px;
  }
  .contact {
    position: absolute; display: flex; align-items: center; gap: 14px;
    font-size: 19px; white-space: nowrap;
  }
  .contact--mobile { left: 44px; top: 112px; }
  .contact--email  { left: 44px; top: 156px; }
  .contact--phone  { left: 580px; top: 370px; font-size: 20px; letter-spacing: 1px; }
  .contact--fax    { left: 580px; top: 412px; font-size: 20px; letter-spacing: 1px; }
  .icon {
    width: 32px; height: 32px; border-radius: 50%; flex: none;
    background: radial-gradient(circle at 35% 30%, var(--blue-light), var(--blue) 55%, var(--blue-deep));
    display: flex; align-items: center; justify-content: center;
  }
  .icon svg { width: 18px; height: 18px; }
  .address {
    position: absolute; right: 36px; bottom: 30px;
    font-family: "Roboto Condensed", "Arial Narrow", sans-serif;
    font-weight: 700; font-size: 26px; white-space: nowrap;
  }
  .brand {
    position: absolute; left: 500px; top: 272px;
    transform: translate(-50%, -50%) rotate(-16.7deg);
    display: flex; align-items: center; gap: 18px; white-space: nowrap;
  }
  .brand__mark { width: 54px; height: 54px; background: var(--blue); }
  .brand__name {
    font-family: "Arimo", Arial, sans-serif; font-weight: 700;
    font-size: 66px; color: var(--ink-dark);
  }
</style>
</head>
<body>
  <div class="card">
    <svg class="card__band" width="900" height="520" viewBox="0 0 900 520">
      <defs>
        <linearGradient id="band-fill" x1="0" y1="1" x2="1" y2="0">
          <stop offset="0" stop-color="var(--band)"/>
          <stop offset="1" stop-color="var(--band-shade)"/>
        </linearGradient>
      </defs>
      <polygon points="0,330 900,60 900,230 0,520" fill="url(#band-fill)"/>
    </svg>

    <h1 class="card__name">Colin Marwood</h1>

    <div class="contact contact--mobile">
      <span class="icon"><svg viewBox="0 0 18 18"><rect x="5" y="1.5" width="8" height="15" rx="1.5" fill="#fff"/><rect x="6.5" y="3.5" width="5" height="6" fill="#1f5fd6"/></svg></span>
      0498 172 943
    </div>
    <div class="contact contact--email">
      <span class="icon"><svg viewBox="0 0 18 18" fill="none" stroke="#fff" stroke-width="1.3"><circle cx="9" cy="9" r="7"/><ellipse cx="9" cy="9" rx="3" ry="7"/><path d="M2 9h14M3 5.5h12M3 12.5h12"/></svg></span>
      col@ridgelinetrusses.com.au
    </div>

    <div class="brand">
      <span class="brand__mark"></span>
      <span class="brand__name">Ridgeline Trusses</span>
    </div>

    <div class="contact contact--phone">
      <span class="icon"><svg viewBox="0 0 18 18"><path d="M5 2l3 3-1.6 1.8a9 9 0 004.8 4.8L13 10l3 3-2 2.5C8 15 3 10 2.5 4z" fill="#fff"/></svg></span>
      02 6812 4300
    </div>
    <div class="contact contact--fax">
      <span class="icon"><svg viewBox="0 0 18 18" fill="#fff"><rect x="5" y="2" width="8" height="5"/><rect x="2" y="7" width="14" height="8" rx="1.5"/><rect x="5" y="10" width="8" height="2" fill="#1f5fd6"/></svg></span>
      02 6812 4900
    </div>

    <p class="address">14 Larchmont Road, Brackenvale NSW 2894</p>
  </div>
</body>
</html>
```